Rings and things/plans. Wedding planning checklist design

We are a wedding videography start-up that's about to launch a chatterly campaign. We need a simple yet premium looking design to showcase a wedding planning checklist which we have written. The main focus of the design should be:

- On A4 pages
- Appeal to young engaged women
- Anyone at home can print it off and stick it onto a fridge
- Premium looking

The contents doesn't have to be on one piece of A4, the list can span more than one page. Also, it doesn't have to be traditional folded brochure style, a full A4 sized list is preferred. The design will potentially be used in further A4 brochure style blog posts. The written checklist and our company logo is attached for reference.

Target Market(s)

Young engaged woman

Industry/Entity Type

Wedding

Requirements
Must have
• Simple and premium feel.
Nice to have
• flexible design that can be reused in the future for blog posts.

```html
<!DOCTYPE html>
<html lang="en">
<head>
<meta charset="utf-8">
<title>Wedding Checklist – 1 Week</title>
<link href="https://fonts.googleapis.com/css2?family=Crimson+Pro:wght@400;700&family=Yellowtail&display=swap" rel="stylesheet">
<style>
  :root {
    --backdrop: #202020;
    --paper: #ffffff;
    --band: #eaf1f9;
    --accent: #2ea3dc;
    --ink: #2f2f33;
    --photo-light: #f3f6fb;
    --photo-mid: #c9d7ec;
    --photo-deep: #aec3e2;
  }
  * { margin: 0; padding: 0; box-sizing: border-box; }
  html, body {
    width: 960px; height: 1200px; overflow: hidden;
    background: var(--backdrop);
  }
  .page {
    position: absolute; left: 56px; top: 0;
    width: 848px; height: 1200px;
    background: var(--paper);
    font-family: "Crimson Pro", Georgia, serif;
    color: var(--ink);
    overflow: hidden;
  }
  .hero-photo {
    position: absolute; left: 0; top: 570px; width: 848px; height: 545px;
    background:
      radial-gradient(ellipse 230px 110px at 555px 320px, #e4ebf5 0%, rgba(228,235,245,0) 100%),
      linear-gradient(180deg, var(--paper) 0%, var(--photo-light) 12%, var(--photo-mid) 40%, var(--photo-deep) 58%, var(--photo-mid) 78%, var(--paper) 100%);
  }
  .stage-label {
    position: absolute; left: 57px; top: 72px; height: 105px;
    width: 52px;
  }
  .stage-label span {
    position: absolute; left: 50%; top: 50%;
    transform: translate(-50%, -50%) rotate(-90deg);
    font-family: "Yellowtail", cursive;
    font-size: 58px; line-height: 1;
    color: var(--accent);
    white-space: nowrap;
  }
  .timeline-rule {
    position: absolute; left: 128px; top: 41px;
    width: 1.5px; height: 533px; background: var(--accent);
  }
  .checklist {
    position: absolute; left: 129px; top: 41px; width: 719px;
    list-style: none;
  }
  .task {
    display: flex; align-items: flex-start;
    padding-top: 19px;
  }
  .task.shaded { background: var(--band); }
  .task-title {
    width: 347px; padding-left: 28px;
    font-size: 18.5px; font-weight: 700; line-height: 25px;
  }
  .task-note {
    width: 300px;
    font-size: 14px; line-height: 19px; padding-top: 2px;
  }
  .h80 { height: 80px; } .h98 { height: 98px; } .h81 { height: 81px; }
  .h84 { height: 84px; } .h110 { height: 110px; }
  .shift { padding-left: 24px; }
  .credits {
    position: absolute; left: 0; top: 990px; width: 848px;
    text-align: center; font-weight: 700; font-size: 21px; line-height: 28px;
  }
  .credits .contact { margin-top: 28px; }
</style>
</head>
<body>
  <main class="page">
    <div class="hero-photo" role="img" aria-label="Soft-focus photo of a diamond engagement ring resting on a wedding band over white lace"></div>

    <div class="stage-label"><span>1 week</span></div>
    <div class="timeline-rule"></div>

    <ul class="checklist">
      <li class="task shaded h80">
        <div class="task-title" style="padding-left:31px">Wedding rehearsal</div>
        <div class="task-note">Don’t forget to time all journeys</div>
      </li>
      <li class="task h98">
        <div class="task-title">Prepare emergency bride &amp;<br>groom kits</div>
        <div class="task-note">These can include toothpaste, painkillers, sanitary pads, needle/safety pins, makeup, tissue, deodorant, nail glue, hair gel etc</div>
      </li>
      <li class="task shaded h81">
        <div class="task-title" style="padding-left:31px">Assign people to pack up after<br>the wedding</div>
        <div class="task-note">Minimize stress on the day by delegating<br>tasks beforehand</div>
      </li>
      <li class="task h84">
        <div class="task-title">Confirm final attendances</div>
        <div class="task-note">Follow up with your guests to make sure there aren’t any last minute cancellations</div>
      </li>
      <li class="task shaded h80">
        <div class="task-title" style="padding-left:31px">Get nails done</div>
        <div class="task-note">Follow up with your guests to make sure<br>there aren’t any last minute cancellations</div>
      </li>
      <li class="task h110">
        <div class="task-title">Pack for your honeymoon</div>
        <div class="task-note">Keep up the wedding buzz by not having<br>to stress about packing</div>
      </li>
    </ul>

    <footer class="credits">
      <p>Written by Mara Ellison<br>Wedding Planner</p>
      <p class="contact">0210004821<br>maraellison21@letterpost.com</p>
    </footer>
  </main>
</body>
</html>
```